Website Design for Amberfold Vista Group – Professional, Modern, and Sustainable Energy Consulting

Amberfold Vista Group is a leading consultancy specializing in sustainable energy solutions. We are seeking a professional and visually appealing Squarespace website design to showcase our expertise and services. The website should reflect our brand identity, as defined by our new logo, and provide an engaging user experience. Please read carefully the attached document "Website product requirement rev 1.pdf".

```html
<!DOCTYPE html>
<html lang="en">
<head>
<meta charset="utf-8">
<title>Amberfold Vista Group – Sustainable Energy Consulting</title>
<link rel="stylesheet" href="https://fonts.googleapis.com/css2?family=Poppins:wght@400;500;600;700;800&display=swap">
<style>
:root{
  --green:#24b574;
  --green-dark:#1e9c63;
  --ink:#111418;
  --text:#555b61;
  --navy:#0d1b2e;
  --navy-2:#162a45;
  --mint:#80ecc0;
  --light:#f4f4f4;
  --white:#ffffff;
}
*{margin:0;padding:0;box-sizing:border-box}
html,body{width:1200px;height:4034px;overflow:hidden}
body{font-family:"Poppins",sans-serif;color:var(--ink);background:var(--white);position:relative}
.abs{position:absolute}
a{color:inherit;text-decoration:none}

/* header */
.site-header{position:absolute;top:0;left:0;width:1200px;height:92px;background:var(--white)}
.brand{position:absolute;left:104px;top:22px;display:flex;align-items:center;gap:10px}
.brand-dot{width:46px;height:46px;border-radius:50%;background:var(--green);flex:none}
.brand-name{font-weight:600;font-size:23px;line-height:1;color:var(--green-dark);white-space:nowrap}
.brand-tag{font-size:7px;letter-spacing:1.4px;color:var(--text);margin-top:5px;white-space:nowrap}
.main-nav{position:absolute;left:480px;top:36px;display:flex;gap:30px;font-size:12.5px;font-weight:500}
.main-nav .active{color:var(--green)}
.lang{position:absolute;left:838px;top:28px;display:flex;align-items:center;gap:6px;font-size:12px;font-weight:600}
.lang-flag{width:34px;height:34px;border-radius:50%;background:linear-gradient(180deg,#c9303c 0 50%,#e9e9ee 50% 100%);position:relative;overflow:hidden}
.lang-flag::after{content:"";position:absolute;left:0;top:0;width:17px;height:17px;background:#2a3f8f}
.btn{display:inline-flex;align-items:center;justify-content:center;gap:8px;background:var(--green);color:var(--white);font-weight:600;font-size:12.5px;text-transform:uppercase;white-space:nowrap}
.btn-ring{width:20px;height:20px;border:2px solid var(--white);border-radius:50%;flex:none}
.header-cta{position:absolute;left:936px;top:22px;width:151px;height:45px}

/* hero */
.hero{position:absolute;top:92px;left:0;width:1200px;height:498px;background:linear-gradient(180deg,#3e5c3a 0%,#4d6f3d 22%,#2d4f8a 40%,#1f3c78 70%,#5c7d2e 100%)}
.hero h1{position:absolute;top:38px;width:100%;text-align:center;color:var(--white);font-weight:800;font-size:57px;letter-spacing:2px}
.hero p{position:absolute;top:100px;width:100%;text-align:center;color:var(--white);font-weight:700;font-size:38px;letter-spacing:12px}
.hero-quote{position:absolute;left:524px;top:173px;width:152px;height:44px;background:rgba(20,30,30,.85);border:2px solid var(--white)}
.arrow-dot{position:absolute;width:26px;height:26px;border-radius:50%;background:var(--white);display:flex;align-items:center;justify-content:center}

/* section headings */
.section-title{position:absolute;left:0;width:100%;text-align:center;font-weight:700;font-size:37px}
.divider{position:absolute;left:50%;transform:translateX(-50%);display:flex;align-items:center;gap:8px}
.divider i{display:block;width:38px;height:2px;background:currentColor}
.divider b{display:block;width:18px;height:18px;border:2px solid var(--green);border-radius:50%}

/* about */
.about-mark{position:absolute;left:162px;top:700px;width:408px;height:400px;border-radius:50%;background:var(--green);display:flex;align-items:center;justify-content:center;color:var(--white);font-weight:600;font-size:30px;text-align:center;line-height:1.25;box-shadow:0 30px 30px -20px rgba(0,0,0,.25)}
.about-copy{position:absolute;left:660px;top:700px;width:390px}
.about-copy h2{font-weight:700;font-size:37px}
.about-copy p{font-size:12.7px;line-height:22px;color:var(--text);margin-top:20px}
.about-copy .btn{margin-top:28px;width:150px;height:44px;font-size:12px}

/* support */
.support{position:absolute;top:1203px;left:0;width:1200px;height:432px;background:linear-gradient(135deg,var(--navy-2),var(--navy) 60%,#0a1424);color:var(--white)}
.support-list{position:absolute;top:212px;left:0;width:1200px}
.support-item{position:absolute;text-align:center;font-weight:700;font-size:16px;width:200px;transform:translateX(-50%)}
.support-item svg{display:block;margin:0 auto 14px;width:64px;height:64px}

/* services */
.card{position:absolute;width:295px}
.card-media{width:295px;height:321px}
.card-title{position:absolute;top:352px;left:0;width:220px;font-weight:700;font-size:16px;line-height:28px}
.card-link{position:absolute;left:236px;top:346px;width:56px;height:56px}

/* testimonials */
.testimonials{position:absolute;top:2855px;left:0;width:1200px;height:540px;background:var(--light)}
.quote-card{position:absolute;top:192px;width:299px;height:223px;background:var(--white);text-align:center;border-radius:3px}
.quote-card.featured{box-shadow:0 6px 20px rgba(0,0,0,.12)}
.avatar{position:absolute;left:50%;top:-34px;transform:translateX(-50%);width:72px;height:72px;border-radius:50%;background:linear-gradient(160deg,#d9c2a8,#8a6a52)}
.quote-card p{position:absolute;top:64px;left:30px;right:30px;font-size:10.5px;line-height:20px;color:var(--text)}
.quote-card hr{position:absolute;top:156px;left:30px;right:30px;border:0;border-top:1px solid #e3e3e3}
.quote-card h4{position:absolute;top:172px;left:0;width:100%;font-size:10px;font-weight:600}
.quote-card .role{position:absolute;top:192px;left:0;width:100%;font-size:10px;color:var(--green);white-space:nowrap}

/* partners */
.partners{position:absolute;top:3395px;left:0;width:1200px;height:302px;background:var(--mint)}
.partner-badge{position:absolute;top:143px;height:62px;border-radius:6px;background:rgba(255,255,255,.35)}

/* footer */
.site-footer{position:absolute;top:3697px;left:0;width:1200px;height:337px;background:linear-gradient(135deg,var(--navy-2),var(--navy));color:var(--white)}
.footer-col{position:absolute;top:80px}
.footer-col h5{font-size:15px;font-weight:600;margin-bottom:18px}
.footer-col li{list-style:none;font-size:12px;line-height:27px;white-space:nowrap}
.footer-rule{position:absolute;left:140px;top:268px;width:920px;border-top:1px solid rgba(255,255,255,.25)}
.copyright{position:absolute;left:0;top:290px;width:100%;text-align:center;font-size:11.5px}
</style>
</head>
<body>

<header class="site-header">
  <div class="brand">
    <div class="brand-dot"></div>
    <div>
      <div class="brand-name">Amberfold Vista Group</div>
      <div class="brand-tag">CONNECTING PEOPLE, POWER, AND PLANET</div>
    </div>
  </div>
  <nav class="main-nav">
    <a class="active">HOME</a><a>ABOUT US</a><a>OUR SERVICES</a><a>BLOG</a>
  </nav>
  <div class="lang"><span class="lang-flag"></span>EN ⌄</div>
  <a class="btn header-cta"><span class="btn-ring"></span>CONTACT US</a>
</header>

<section class="hero" role="img" aria-label="Engineer in a hard hat walking between rows of solar panels in a green field">
  <h1>CONNECTING</h1>
  <p>People, Power, and Planet</p>
  <a class="btn hero-quote"><span class="btn-ring"></span>GET A QUOTE</a>
  <span class="arrow-dot" style="left:64px;top:265px"><svg width="12" height="12" viewBox="0 0 12 12"><path d="M8 1 3 6l5 5" fill="none" stroke="#111" stroke-width="2.5"/></svg></span>
  <span class="arrow-dot" style="left:1110px;top:265px"><svg width="12" height="12" viewBox="0 0 12 12"><path d="M4 1l5 5-5 5" fill="none" stroke="#111" stroke-width="2.5"/></svg></span>
</section>

<section class="about">
  <div class="about-mark">Amberfold<br>Vista Group</div>
  <div class="about-copy">
    <h2>ABOUT US</h2>
    <div class="divider" style="position:relative;left:38px;transform:none;margin-top:6px;color:#111"><i></i><b></b><i></i></div>
    <p>Starting as novices in 1993, we have worked on every aspect of a project's life cycle, from concept to commissioning, in order to become today's experts.</p>
    <p style="margin-top:16px">Elias Moreno is a dynamic, solution-focused technical leader with more than 24 years of international experience in solar PV, project management, installation and engineering across LATAM, Spain, Canada and USA. Elias has a proven track record delivering and directing key technical aspects in support of business development and project development.</p>
    <a class="btn" style="display:flex"><span class="btn-ring"></span>LEARN MORE</a>
  </div>
</section>

<section class="support">
  <h2 class="section-title" style="top:95px;color:#fff">COMPREHENSIVE SUPPORT</h2>
  <div class="divider" style="top:150px;color:#fff"><i></i><b></b><i></i></div>
  <div class="support-list">
    <div class="support-item" style="left:203px">
      <svg viewBox="0 0 64 64" fill="none" stroke="#24b574" stroke-width="2.5"><rect x="10" y="8" width="44" height="46" rx="3"/><path d="M18 46V36M26 46V30M34 46V34M42 46V24M16 28l10-8 8 6 12-12"/></svg>
      PROJECT DEVELOPER</div>
    <div class="support-item" style="left:425px">
      <svg viewBox="0 0 64 64" fill="none" stroke="#24b574" stroke-width="2.5"><circle cx="16" cy="40" r="5"/><circle cx="32" cy="36" r="5"/><circle cx="48" cy="40" r="5"/><path d="M6 56c0-6 5-9 10-9s10 3 10 9M22 56c0-7 5-11 10-11s10 4 10 11M38 56c0-6 5-9 10-9s10 3 10 9M14 24l12-8 8 6 16-12M44 10h6v6"/></svg>
      INVESTOR</div>
    <div class="support-item" style="left:602px">
      <svg viewBox="0 0 64 64" fill="none" stroke="#24b574" stroke-width="2.5"><path d="M24 8h16l-4 8h-8zM28 16c-10 6-12 20 4 22 16-2 14-16 4-22"/><path d="M8 50l10-6h14l8 4M8 58l12-4 22 2 14-10"/><path d="M32 22v12"/></svg>
      LENDER</div>
    <div class="support-item" style="left:771px">
      <svg viewBox="0 0 64 64" fill="none" stroke="#24b574" stroke-width="2.5"><path d="M6 30C8 14 20 6 32 6s24 8 26 24c-4-4-8-4-12 0-4-4-10-4-14 0-4-4-10-4-14 0-4-4-8-4-12 0zM32 6v24"/><circle cx="22" cy="42" r="4"/><circle cx="42" cy="42" r="4"/><circle cx="32" cy="40" r="4"/><path d="M14 58c0-6 4-9 8-9s8 3 8 9M34 58c0-6 4-9 8-9s8 3 8 9"/></svg>
      INSURANCE</div>
    <div class="support-item" style="left:985px">
      <svg viewBox="0 0 64 64" fill="none" stroke="#24b574" stroke-width="2.5"><path d="M28 6h8l2 7 6 3 7-3 5 6-4 6 1 7 6 4-3 8-7-1-5 5 1 7-8 3-4-6h-7l-4 6-8-3 1-7-5-5-7 1-3-8 6-4 1-7-4-6 5-6 7 3 6-3z"/><path d="M22 42l16-16M36 20l8 8"/></svg>
      UTILITY&nbsp; COMPANY</div>
  </div>
</section>

<section class="services">
  <h2 class="section-title" style="top:1720px">OUR SERVICES</h2>
  <div class="divider" style="top:1770px;color:#111"><i></i><b></b><i></i></div>

  <article class="card" style="left:114px;top:1815px">
    <div class="card-media" role="img" aria-label="Solar panels at sunset" style="background:linear-gradient(160deg,#f3b451 0%,#6a8fb8 35%,#1d3f7a 100%)"></div>
    <h3 class="card-title">PROJECT DEVELOPMENT TECHNICAL ADVISOR</h3>
    <svg class="card-link" viewBox="0 0 56 56"><path d="M28 4a24 24 0 1 1-22 14" fill="none" stroke="#24b574" stroke-width="5"/><path d="M18 36l8-8 5 5 9-9M34 24h6v6" fill="none" stroke="#333" stroke-width="2"/></svg>
  </article>
  <article class="card" style="left:453px;top:1815px">
    <div class="card-media" role="img" aria-label="Two engineers reviewing plans beside solar panels" style="background:linear-gradient(180deg,#bcd3ea 0%,#6f94c0 35%,#244c85 65%,#4f7a34 100%)"></div>
    <h3 class="card-title">PERFORMING SYSTEM OPTIMIZATION</h3>
    <svg class="card-link" viewBox="0 0 56 56"><path d="M28 4a24 24 0 1 1-22 14" fill="none" stroke="#24b574" stroke-width="5"/><path d="M18 36l8-8 5 5 9-9M34 24h6v6" fill="none" stroke="#333" stroke-width="2"/></svg>
  </article>
  <article class="card" style="left:791px;top:1815px">
    <div class="card-media" role="img" aria-label="Solar array under a blue sky with clouds" style="background:linear-gradient(180deg,#4b86c9 0%,#9fc0e2 40%,#2a4f8f 65%,#4a6b35 100%)"></div>
    <h3 class="card-title">RUNNING ENERGY SIMULATION</h3>
    <svg class="card-link" viewBox="0 0 56 56"><path d="M28 4a24 24 0 1 1-22 14" fill="none" stroke="#24b574" stroke-width="5"/><path d="M18 36l8-8 5 5 9-9M34 24h6v6" fill="none" stroke="#333" stroke-width="2"/></svg>
  </article>

  <article class="card" style="left:114px;top:2252px">
    <div class="card-media" role="img" aria-label="Hard hat resting on a solar panel beside plans" style="background:linear-gradient(170deg,#5a8a3c 0%,#2c4f86 40%,#d6dde6 100%)"></div>
    <h3 class="card-title">DESIGNING THE PLANT LAYOUT</h3>
    <svg class="card-link" viewBox="0 0 56 56"><path d="M28 4a24 24 0 1 1-22 14" fill="none" stroke="#24b574" stroke-width="5"/><path d="M18 36l8-8 5 5 9-9M34 24h6v6" fill="none" stroke="#333" stroke-width="2"/></svg>
  </article>
  <article class="card" style="left:453px;top:2252px">
    <div class="card-media" role="img" aria-label="Close view of tilted solar panels against the sky" style="background:linear-gradient(150deg,#8fb6df 0%,#2b4f8d 45%,#1b3566 80%,#7a8a6a 100%)"></div>
    <h3 class="card-title">PROJECT PLANNING AND COST ANALYSIS</h3>
    <svg class="card-link" viewBox="0 0 56 56"><path d="M28 4a24 24 0 1 1-22 14" fill="none" stroke="#24b574" stroke-width="5"/><path d="M18 36l8-8 5 5 9-9M34 24h6v6" fill="none" stroke="#333" stroke-width="2"/></svg>
  </article>
  <article class="card" style="left:791px;top:2252px">
    <div class="card-media" role="img" aria-label="Large solar farm in a desert valley at dusk" style="background:linear-gradient(180deg,#e9c99a 0%,#b58a5e 35%,#3b4a66 60%,#8a6a45 100%)"></div>
    <h3 class="card-title">DILIGENCE IN SUPPORT OF PROJECT ACQUISITION</h3>
    <svg class="card-link" viewBox="0 0 56 56"><path d="M28 4a24 24 0 1 1-22 14" fill="none" stroke="#24b574" stroke-width="5"/><path d="M18 36l8-8 5 5 9-9M34 24h6v6" fill="none" stroke="#333" stroke-width="2"/></svg>
  </article>

  <a class="btn abs" style="left:490px;top:2695px;width:220px;height:45px;font-size:12px"><span class="btn-ring"></span>LEARN MORE SERVICES</a>
</section>

<section class="testimonials">
  <h2 class="section-title" style="top:75px">OUR TESTIMONIALS</h2>
  <div class="divider" style="top:125px;color:#111"><i></i><b></b><i></i></div>

  <div class="quote-card" style="left:108px">
    <div class="avatar" role="img" aria-label="Portrait of Dana Whitcombe"></div>
    <p>Elias has a very strong technical understanding of solar power plant development and execution, based on a long track record in the industry...</p>
    <hr><h4>DANA WHITCOMBE</h4><div class="role">VP Engineering Kestrel Power</div>
  </div>
  <div class="quote-card featured" style="left:449px">
    <div class="avatar" role="img" aria-label="Portrait of Ravi Castellan"></div>
    <p>Beyond his technical capabilities and industry knowledge, Elias is a hard working, self-motivated person who can be counted on to put the project and team needs first.</p>
    <hr><h4>RAVI CASTELLAN</h4><div class="role">COO at Brightfield Solar, LLC</div>
  </div>
  <div class="quote-card" style="left:789px">
    <div class="avatar" role="img" aria-label="Portrait of Dana Whitcombe"></div>
    <p>Elias has a very strong technical understanding of solar power plant development and execution, based on a long track record in the industry...</p>
    <hr><h4>DANA WHITCOMBE</h4><div class="role">VP Engineering Kestrel Power</div>
  </div>

  <span class="arrow-dot" style="left:64px;top:281px;background:var(--green)"><svg width="12" height="12" viewBox="0 0 12 12"><path d="M8 1 3 6l5 5" fill="none" stroke="#fff" stroke-width="2.5"/></svg></span>
  <span class="arrow-dot" style="left:1110px;top:281px;background:#111"><svg width="12" height="12" viewBox="0 0 12 12"><path d="M4 1l5 5-5 5" fill="none" stroke="#fff" stroke-width="2.5"/></svg></span>
</section>

<section class="partners">
  <h2 class="section-title" style="top:70px">OUR PARTNERS</h2>
  <div class="divider" style="top:120px;color:#111"><i></i><b></b><i></i></div>
  <div class="partner-badge" style="left:108px;width:130px"></div>
  <div class="partner-badge" style="left:314px;width:150px"></div>
  <div class="partner-badge" style="left:530px;width:140px"></div>
  <div class="partner-badge" style="left:752px;width:100px"></div>
  <div class="partner-badge" style="left:918px;width:150px"></div>
</section>

<footer class="site-footer">
  <div class="brand" style="left:106px;top:118px">
    <div class="brand-dot"></div>
    <div>
      <div class="brand-name" style="color:#fff">Amberfold Vista Group</div>
      <div class="brand-tag" style="color:#cfd6de">CONNECTING PEOPLE, POWER, AND PLANET</div>
    </div>
  </div>
  <div class="footer-col" style="left:471px">
    <h5>QUICK LINKS</h5>
    <ul><li>HOME</li><li>ABOUT US</li><li>OUR SERVICES</li><li>OUR EXPERIENCE</li><li>CONTACT US</li></ul>
  </div>
  <div class="footer-col" style="left:668px">
    <h5>CONTACT US</h5>
    <ul><li>(415) 555-0142</li><li style="margin-top:6px">ELIAS.MORENO@AMBERFOLD.WORK</li></ul>
  </div>
  <div class="footer-col" style="left:927px">
    <h5>SOCAIL MEDIA</h5>
    <ul><li style="line-height:25px">FACEBOOK</li><li style="line-height:25px">INSTAGRAM</li><li style="line-height:25px">LINKED IN</li></ul>
  </div>
  <div class="footer-rule"></div>
  <div class="copyright">Copyright@2024 - &nbsp;All Rights Reserved By AVG</div>
</footer>

</body>
</html>
```